Brume d'Orvelle Hand Crafted Candles promotional flyer

Hand Crafted Soy Candles - I need a flyer to promote my candles and to give information on care of candles.I want this to use the design and colours I already have for my labels and the photo I have attached.I am aiming at a sophisticated market so would like to reflect this in the design.
Should appeal to sophisticated women who enjoy the pleasure of candles - to enhance their enjoyment of life - gives them the 'brume d'orvelle'.
the candles are hand crafted from all natural ingredients, environmentally friendly and with exquisite fragrances

Target Market(s)

sophisticated females

Industry/Entity Type

Promotional

Font styles to use
Script

Colors
cfeae6
ecdaeb

Requirements
Must have
• something expressing 'brume d'orvelle' - the enjoyment of candles
Should not have
• bright colours

```html
<!DOCTYPE html>
<html lang="en">
<head>
<meta charset="utf-8">
<title>Brume d'Orvelle Hand Crafted Candles – Flyer</title>
<link href="https://fonts.googleapis.com/css2?family=Pinyon+Script&family=Mulish:wght@400;600;700;800&family=Exo+2:wght@600&family=Cormorant+SC:wght@500&display=swap" rel="stylesheet">
<style>
:root{
  --stage:#e6e0ea;
  --night:#1c1230;
  --night-2:#2e2150;
  --night-3:#3d2d63;
  --gold:#d4a43c;
  --gold-light:#f3d68a;
  --lilac:#ecdaeb;
  --lilac-2:#e3d0ea;
  --mint:#cfeae6;
  --cream:#f4efcf;
  --cream-2:#efe6bf;
  --ink:#2b2233;
  --maroon:#7a3440;
  --label:#e9eef0;
  --white:#ffffff;
}
*{box-sizing:border-box;margin:0;padding:0}
html,body{width:1041px;height:1200px;overflow:hidden;background:var(--stage)}
body{position:relative;font-family:"Mulish",sans-serif;color:var(--ink)}
.flyer{position:absolute;left:70px;top:19px;width:900px;height:1162px;overflow:hidden;background:var(--night);box-shadow:0 10px 30px rgba(40,20,60,.25)}
.hero{position:absolute;left:0;top:0;width:900px;height:470px;background:radial-gradient(ellipse at 40% 40%,var(--night-3),var(--night) 75%)}
.brand-mark{position:absolute;left:190px;top:18px;width:244px;height:214px}
.brand-mark circle{fill:var(--label)}
.brand-mark text{font-family:"Mulish",sans-serif;font-weight:700;font-size:27px;fill:var(--night-2)}
.candle-photo{position:absolute;left:35px;top:262px;width:495px;height:165px;border-radius:6px;
  background:linear-gradient(90deg,#15131c 0 22%,#d9cf9a 24% 45%,#e9e6b4 50% 72%,#2a3d8a 76% 92%,transparent 94%);opacity:.85}
.model-photo{position:absolute;left:551px;top:30px;width:349px;height:440px;
  background:radial-gradient(circle at 42% 68%,#ffd9a8 0,#e7a8b8 9%,transparent 22%),radial-gradient(ellipse at 45% 30%,#d9b98a 0,#8d7aa0 38%,var(--night-2) 70%)}
.wave{position:absolute;left:0;top:400px;width:900px;height:80px;z-index:2}
.lower{position:absolute;left:0;top:420px;width:900px;height:672px;display:flex}
.intro{width:493px;height:100%;background:linear-gradient(180deg,var(--lilac) 0,var(--lilac-2) 60%,var(--mint) 100%);padding:50px 26px 0 40px;position:relative}
.care{flex:1;height:100%;background:linear-gradient(180deg,var(--cream) 0,var(--cream-2) 100%);padding:58px 22px 0 14px}
.title{font-family:"Pinyon Script",cursive;font-size:50px;line-height:1;color:var(--night);margin-left:8px}
.subtitle{font-family:"Cormorant SC",serif;font-size:17px;letter-spacing:.5px;color:var(--night);text-align:right;padding-right:54px;border-bottom:1px solid #9b8aa6;padding-bottom:3px;margin-bottom:7px}
.points{list-style:none;font-size:13.8px;line-height:1.15}
.points li{position:relative;padding-left:17px;margin-bottom:4px}
.points li::before{content:"";position:absolute;left:2px;top:6px;width:6px;height:6px;border-radius:50%;background:var(--maroon)}
.intro .lead li{max-width:292px}
.section-head{font-weight:800;font-size:18px;color:var(--maroon);margin:13px 0 4px 16px}
.points.spaced li{margin-bottom:8px}
.jar-photo{position:absolute;left:345px;top:200px;width:128px;height:140px;border-radius:10px 10px 14px 14px;
  background:radial-gradient(ellipse at 50% 45%,var(--label) 0 33%,#101018 35%)}
.care-head{font-weight:800;font-style:italic;font-size:14px;line-height:1.17;color:var(--maroon);padding-left:14px;margin-bottom:14px}
.steps{list-style:none;counter-reset:step}
.steps li{counter-increment:step;position:relative;padding-left:28px;font-size:12.6px;line-height:1.16;margin-bottom:14.5px}
.steps li::before{content:counter(step);position:absolute;left:0;top:-1px;width:19px;height:19px;border-radius:50%;background:var(--maroon);color:var(--white);font-weight:800;font-size:12px;text-align:center;line-height:19px}
.footer{position:absolute;left:0;top:1092px;width:900px;height:70px;background:var(--night);border-top:2px solid var(--gold);display:flex;align-items:center;font-family:"Exo 2",sans-serif;color:var(--white)}
.phone{display:flex;align-items:center;gap:10px;font-size:27px;letter-spacing:1px;margin-left:96px;width:470px}
.contacts{font-size:15.5px;line-height:1.45}
.contacts div{display:flex;align-items:center;gap:9px}
</style>
</head>
<body>
<main class="flyer">
  <section class="hero">
    <svg class="brand-mark" viewBox="0 0 244 214" aria-label="Brume d'Orvelle">
      <circle cx="122" cy="107" r="106"/>
      <text x="122" y="116" text-anchor="middle">Brume d'Orvelle</text>
    </svg>
    <div class="candle-photo" role="img" aria-label="Photo of four labelled soy candles in glass jars"></div>
    <div class="model-photo" role="img" aria-label="Photo of a woman holding a lit candle in her hands"></div>
  </section>

  <svg class="wave" viewBox="0 0 900 80" preserveAspectRatio="none" aria-hidden="true">
    <path d="M0 0 H900 V24 Q450 100 0 18 Z" fill="var(--night)"/>
    <path d="M0 18 Q450 100 900 24" fill="none" stroke="var(--gold)" stroke-width="5"/>
    <path d="M0 24 Q450 104 900 30" fill="none" stroke="var(--gold-light)" stroke-width="1.5"/>
  </svg>

  <section class="lower">
    <div class="intro">
      <h1 class="title">Brume d'Orvelle</h1>
      <p class="subtitle">Hand Crafted Soy Candles</p>
      <ul class="points lead">
        <li>Brume d'Orvelle – an exuberant enjoyment of life – these candles will fill you with "Brume d'Orvelle".</li>
        <li>Candles are lovingly hand-poured and use only the finest of ingredients and fragrances</li>
        <li>Hand crafted soy candle creations</li>
        <li>Completely non-toxic</li>
        <li>Exquisite fragrances</li>
        <li>Clean burning</li>
        <li>Environmentally friendly.</li>
      </ul>
      <div class="jar-photo" role="img" aria-label="Photo of a black candle jar with label"></div>

      <h2 class="section-head">Why soy wax?</h2>
      <ul class="points">
        <li>Soft smooth wax that burns clear – no soot or smoke</li>
        <li>Soy wax candles burn up to 50% longer than traditional paraffin candles</li>
        <li>Made from soya beans, a renewable natural resource that supports and sustains agriculture – it is biodegradable and environmentally friendly.</li>
        <li>Soy wax burns cooler than paraffin and disperse the fragrance more fully.</li>
      </ul>

      <h2 class="section-head">Containers can be refilled</h2>
      <ul class="points spaced">
        <li>I offer a refill service - if you return your containers to me I can refill with the fragrance of your choice</li>
        <li>Or if you have a special container you would like to use for your candle just contact me for a quote.</li>
        <li>I have a wide range of fragrances - please contact me for details.</li>
      </ul>
    </div>

    <div class="care">
      <p class="care-head">How to care for your candle – the following tips will ensure you have a long lasting, fully fragranced candle</p>
      <ol class="steps">
        <li>When lighting your candle for the first time, allow the wax to melt all the way to the sides of the container – this creates a 'memory' and avoids 'tunnelling' as the candle burns.</li>
        <li>Always trim the wick to about 6-8mm before re-lighting your candle. This will ensure a long lasting candle, minimise soot and remove any mushrooming of the wick from a previous burn.</li>
        <li>It is preferable to use a candle 'snuffer' to extinguish the flame, or a lid if the candle has one. Alternatively, you can dip the wick into the melted wax and then straightening. This will stop the wick from smoking and help with relighting.</li>
        <li>All Brume d'Orvelle candles are hand poured not mass produced – although every effort is made to ensure consistency, every candle may be different.</li>
        <li>Sometimes you may notice darker patches or wet spots - this is not a fault it is just the natural way the wax has set – it does not affect the candle in anyway.</li>
        <li>The top of the candle may also appear slightly uneven – this is just a sign of natural soy wax being hand poured.</li>
        <li>Do not leave your candle in the sunlight as it may turn a yellow colour – again this does not affect the candle in anyway – it just loses its creamy white colour.</li>
        <li>As these candles contain no preservatives or chemicals it is recommended that they should be used within 6 months.</li>
      </ol>
    </div>
  </section>

  <footer class="footer">
    <div class="phone">
      <svg width="24" height="24" viewBox="0 0 24 24" aria-hidden="true"><path d="M6.6 10.8a15 15 0 0 0 6.6 6.6l2.2-2.2c.3-.3.7-.4 1-.2 1.1.4 2.3.6 3.6.6.6 0 1 .4 1 1V20c0 .6-.4 1-1 1A17 17 0 0 1 3 4c0-.6.4-1 1-1h3.5c.6 0 1 .4 1 1 0 1.3.2 2.5.6 3.6.1.3 0 .7-.2 1z" fill="var(--white)"/></svg>
      <span>021 555 0184</span>
    </div>
    <div class="contacts">
      <div><svg width="18" height="13" viewBox="0 0 18 13" aria-hidden="true"><rect x="0.5" y="0.5" width="17" height="12" fill="none" stroke="var(--white)"/><path d="M1 1l8 6 8-6" fill="none" stroke="var(--white)"/></svg>clara.ashdown@mailbox.co.nz</div>
      <div><svg width="18" height="18" viewBox="0 0 18 18" aria-hidden="true"><circle cx="9" cy="9" r="7.5" fill="none" stroke="var(--white)" stroke-width="1.5"/><path d="M1.5 9h15M9 1.5c-3 3.5-3 11.5 0 15M9 1.5c3 3.5 3 11.5 0 15" fill="none" stroke="var(--white)"/></svg>www.mybrumedorvelle.co.nz</div>
    </div>
  </footer>
</main>
</body>
</html>
```